Flyer Advertisement Design for exotic rental company

Design an advertisement for a exotic rental company:

https://zoomvela.com/

Here is a similar business:

https://www.gildmarquerides.com/

I rent out a vehicle called a Tundrix Whipcraft. Here is a link to the manufacturer website:

https://whipcraft.tundrix.com/en-us/

I have the 2018 Tundrix Whipcraft GT in the colors Navy Blue and Sunset Red

This advertisement will be printed on a flyer and placed in strategic locations to attract customers. I am looking for something that will draw the customer in. Please use your imagination and come up with something awesome!

Target Market(s)

Outgoing individuals looking to have some fun! This advertisement will be placed in a country club

Industry/Entity Type

Rental Car

Font styles to use
Serif
Sans Serif
Decorative
Script

Colors

Designer to choose colors to be used in the design.

Requirements
Must have
• Pictures of the Tundrix Whipcraft, website info, message about discount to Hollowbrook Country Club Members, phone number, anything else you feel will make the advertisement look great
Nice to have
• Anything you suggest in your professional capacity
Should not have
• Anything goes!

```html
<!DOCTYPE html>
<html lang="en">
<head>
<meta charset="utf-8">
<title>Zoomvela – Exotic car rentals flyer</title>
<link href="https://fonts.googleapis.com/css2?family=Sorts+Mill+Goudy&family=Jost:ital,wght@0,400;1,800&display=swap" rel="stylesheet">
<style>
  :root {
    --backdrop: #e9e8e6;
    --ink-deep: #050505;
    --ink-mid: #262626;
    --paper: #ffffff;
    --racing-red: #d8232f;
    --vehicle-red: #8e1418;
    --vehicle-shadow: #1a0506;
  }
  * { margin: 0; padding: 0; box-sizing: border-box; }
  html, body { width: 1200px; height: 1148px; overflow: hidden; background: var(--backdrop); }
  .flyer {
    position: absolute;
    left: 20px;
    top: 174px;
    width: 1160px;
    height: 800px;
    overflow: hidden;
    background: radial-gradient(ellipse 65% 70% at 55% 35%, var(--ink-mid) 0%, #151515 50%, var(--ink-deep) 100%);
    color: var(--paper);
  }
  .vehicle-photo {
    position: absolute;
    left: 0;
    top: 25px;
    width: 500px;
    height: 450px;
    background: radial-gradient(ellipse 60% 55% at 42% 50%, var(--vehicle-red) 0%, #5a0c10 45%, var(--vehicle-shadow) 80%, transparent 100%);
  }
  .headline {
    position: absolute;
    left: 75px;
    top: 500px;
    font-family: "Sorts Mill Goudy", serif;
    font-size: 56px;
    font-weight: 400;
    letter-spacing: -0.5px;
  }
  .contact {
    position: absolute;
    left: 78px;
    top: 580px;
    font-family: "Sorts Mill Goudy", serif;
    font-size: 34px;
    line-height: 1.1;
  }
  .member-offer {
    position: absolute;
    left: 82px;
    top: 690px;
    font-family: "Jost", sans-serif;
    font-size: 20px;
    line-height: 1.4;
    letter-spacing: -0.3px;
  }
  .stripes { position: absolute; left: 0; top: 0; }
  .slogan {
    font-family: "Jost", sans-serif;
    font-style: italic;
    font-weight: 800;
    font-size: 50px;
    fill: var(--paper);
  }
  .site-corner {
    position: absolute;
    right: 30px;
    bottom: 48px;
    font-family: "Sorts Mill Goudy", serif;
    font-size: 22px;
  }
</style>
</head>
<body>
<main class="flyer">
  <div class="vehicle-photo" role="img" aria-label="Front view of a red Tundrix Whipcraft GT three-wheeled roadster emerging from the dark"></div>

  <h1 class="headline">Exotic car rentals</h1>

  <p class="contact">www.zoomvela.com<br>555-014-2273</p>

  <p class="member-offer">20% Off for all Hollowbrook Country<br>Club Members<br>www.zoomvela.com/HollowbrookCC</p>

  <svg class="stripes" width="1160" height="800" viewBox="0 0 1160 800">
    <polygon points="700,800 1160,545 1160,590 781,800" fill="var(--racing-red)"/>
    <polygon points="850,800 1160,628 1160,645 881,800" fill="var(--racing-red)"/>
    <text class="slogan" x="0" y="0" textLength="500" lengthAdjust="spacingAndGlyphs" transform="translate(700 778) rotate(-29)">Earn your racing stripes</text>
  </svg>

  <p class="site-corner">www.zoomvela.com</p>
</main>
</body>
</html>
```